Real Estate "For Sale" Sign for construction company

We need a sign that we can use to hang on a post and place on the road when we sell a property. The sign will be simple and will need to mainly feature our logo (files attached), as well as the words "For Sale", and then our phone number "(555) 617 3489". The sign will hang on a post that'll look something like the attached picture.

Target Market(s)

Home buyers

Industry/Entity Type

Real Estate

Font styles to use
Serif
Sans Serif

Colors
0054AA
0677BA
7BADD7
CADEEF
E8F1F8
0094D4
00A9DD
6FCCEA
C7EBF8
E9F6FB

Requirements
Must have
• For Sale & our phone number

```html
<!DOCTYPE html>
<html lang="en">
<head>
<meta charset="utf-8">
<title>For Sale Yard Sign</title>
<link rel="stylesheet" href="https://fonts.googleapis.com/css2?family=Cinzel:wght@400;500&family=Marcellus&display=swap">
<style>
  :root {
    --page-bg: #ffffff;
    --sky-light: #a9def9;
    --sky-mid: #6ec6f2;
    --sky-soft: #9ed9f7;
    --ink-blue: #0054aa;
    --brand-blue: #0677ba;
    --brand-dot: #0094d4;
  }
  html, body {
    margin: 0;
    padding: 0;
    width: 1200px;
    height: 1200px;
    overflow: hidden;
    background: var(--page-bg);
  }
  .canvas {
    position: relative;
    width: 1200px;
    height: 1200px;
  }
  .yard-sign {
    position: absolute;
    left: 250px;
    top: 102px;
    width: 700px;
    height: 996px;
    display: block;
  }
  .band-top { fill: var(--sky-light); }
  .band-feature { fill: var(--sky-mid); }
  .band-contact { fill: var(--sky-soft); }
  .band-foot { fill: var(--sky-mid); }
  .brand-dot { fill: var(--brand-dot); }
  .brand-name {
    font-family: "Cinzel", serif;
    font-weight: 500;
    font-size: 21px;
    fill: var(--brand-blue);
    letter-spacing: 1px;
  }
  .headline {
    font-family: "Cinzel", serif;
    font-weight: 400;
    font-size: 262px;
    fill: var(--ink-blue);
  }
  .phone {
    font-family: "Marcellus", serif;
    font-size: 92px;
    fill: var(--ink-blue);
  }
</style>
</head>
<body>
<main class="canvas">
  <svg class="yard-sign" viewBox="0 0 700 996" xmlns="http://www.w3.org/2000/svg" aria-label="For Sale sign">
    <rect class="band-top" x="0" y="0" width="700" height="500"/>
    <rect class="band-feature" x="0" y="500" width="700" height="296"/>
    <rect class="band-contact" x="0" y="796" width="700" height="126"/>
    <rect class="band-foot" x="0" y="922" width="700" height="74"/>

    <g class="brand">
      <circle class="brand-dot" cx="213" cy="141" r="9"/>
      <text class="brand-name" x="234" y="149" textLength="260" lengthAdjust="spacingAndGlyphs">Laurel Hollow Realty</text>
    </g>

    <text class="headline headline-for" x="113" y="444" textLength="498" lengthAdjust="spacingAndGlyphs">FOR</text>
    <text class="headline headline-sale" x="79" y="744" textLength="553" lengthAdjust="spacingAndGlyphs">SALE</text>

    <text class="phone" x="75" y="891" textLength="552" lengthAdjust="spacingAndGlyphs">(555) 617 3489</text>
  </svg>
</main>
</body>
</html>
```